looking for sleek business card to standout from the crowd!

We are a young biotechnology company looking to help you personalize your health through understanding your genetic make up. We need you help in making a clean but sleek business card design using our new logo. The goal? Any time we give our cards out, people say "nice card!" The feel we are going for is "modern-techy". We don't want to come across as an old, giant pharma company, but not trying to be a hipster either.

Target Market(s)

healthcare and biotechnology industry.

Industry/Entity Type

Biotechnology

Contact Information for Business Card

Info to include on the card will be NAME, TITLE, EMAIL, PHONE. The companies website (www.corvalinbio.com) should also be on the card some where. Would like the logo, when printed, to be raised.

Requirements
Must have
• The logo we have attached in the color it is in. Fonts for text should lean toward more professional/tech.
Nice to have
• Prefer white/light color background
Should not have
• cartoons, landscape backgrounds images.

```html
<!DOCTYPE html>
<html lang="en">
<head>
<meta charset="utf-8">
<title>Corvalin Business Card</title>
<link rel="stylesheet" href="https://fonts.googleapis.com/css2?family=Open+Sans:wght@400;600&display=swap">
<style>
  :root {
    --page-bg: #ecebe8;
    --card-white: #ffffff;
    --band-blue: #3aa0d5;
    --band-blue-dark: #2b8cc4;
    --accent-green: #7cbf3a;
    --ink: #3a3a3a;
    --frame-blue: #3a7fc1;
  }
  * { margin: 0; padding: 0; box-sizing: border-box; }
  html, body { width: 1200px; height: 804px; overflow: hidden; }
  body {
    background: var(--page-bg);
    font-family: "Open Sans", Arial, sans-serif;
    position: relative;
  }
  .card {
    position: absolute;
    width: 520px;
    height: 300px;
    background: var(--card-white);
    box-shadow: 0 6px 18px rgba(0,0,0,0.12);
    overflow: hidden;
  }
  .card-front { left: 50px; top: 252px; }
  .card-back { left: 630px; top: 252px; }

  .frame {
    position: absolute;
    inset: 12px;
    border: 1px solid var(--frame-blue);
    pointer-events: none;
  }

  /* Front */
  .contact-band {
    position: absolute;
    top: 0; right: 0; bottom: 0;
    width: 205px;
    background: linear-gradient(160deg, var(--band-blue), var(--band-blue-dark));
    color: #fff;
    padding: 46px 20px 0 26px;
    font-size: 11.5px;
  }
  .contact-band ul { list-style: none; }
  .contact-band li {
    display: flex;
    align-items: center;
    gap: 8px;
    margin-bottom: 9px;
    letter-spacing: 0.2px;
    white-space: nowrap;
  }
  .contact-band svg { width: 11px; height: 11px; flex: none; fill: #fff; }
  .contact-band .phones { position: absolute; left: 26px; bottom: 44px; }
  .band-motif {
    position: absolute;
    left: 26px; top: 132px;
    width: 22px; height: 16px;
    background: rgba(255,255,255,0.75);
    border-radius: 3px;
  }

  .company-name {
    font-weight: 600;
    color: var(--ink);
    letter-spacing: 2px;
    white-space: nowrap;
  }
  .card-front .company-name {
    position: absolute;
    right: 225px; top: 44px;
    font-size: 18px;
  }

  .identity {
    position: absolute;
    left: 58px; top: 150px;
  }
  .identity .name {
    font-size: 23px;
    font-weight: 400;
    color: var(--ink);
  }
  .identity .title {
    font-size: 12px;
    color: var(--accent-green);
    margin-top: 2px;
  }

  /* Back */
  .card-back .frame { inset: 10px; }
  .motif-row {
    position: absolute;
    left: 40px; right: 40px; top: 24px;
    height: 14px;
    background: linear-gradient(90deg, rgba(124,191,58,0.35), rgba(124,191,58,0.6), rgba(124,191,58,0.35));
    border-radius: 7px;
  }
  .card-back .company-name {
    position: absolute;
    left: 50%; top: 50%;
    transform: translate(-50%, -50%);
    font-size: 36px;
    letter-spacing: 4px;
  }
</style>
</head>
<body>
  <section class="card card-front" aria-label="Business card front">
    <div class="frame"></div>
    <p class="company-name">CORVALIN</p>
    <div class="identity">
      <p class="name">Your Name</p>
      <p class="title">Designation</p>
    </div>
    <div class="contact-band">
      <ul>
        <li>
          <svg viewBox="0 0 12 12"><circle cx="6" cy="6" r="5.2" fill="none" stroke="#fff" stroke-width="1.3"/><path d="M1 6h10M6 1c2 2 2 8 0 10M6 1c-2 2-2 8 0 10" fill="none" stroke="#fff" stroke-width="1"/></svg>
          <span>www.corvalinbio.com</span>
        </li>
        <li>
          <svg viewBox="0 0 12 12"><path d="M6 0.5a4 4 0 0 0-4 4c0 3 4 7 4 7s4-4 4-7a4 4 0 0 0-4-4zm0 5.5a1.5 1.5 0 1 1 0-3 1.5 1.5 0 0 1 0 3z"/></svg>
          <span>Lorem ipsum is simply</span>
        </li>
      </ul>
      <div class="band-motif" role="img" aria-label="Small DNA helix motif"></div>
      <ul class="phones">
        <li>
          <svg viewBox="0 0 12 12"><path d="M2.5 0.8l2 2.2-1.2 1.5c.8 1.7 2.2 3.1 3.9 3.9L8.7 7.2l2.3 2-1.1 2C5.5 11 1 6.5.8 2z"/></svg>
          <span>555-214-0187</span>
        </li>
        <li>
          <svg viewBox="0 0 12 12"><rect x="1" y="3" width="10" height="7" rx="1.5"/><path d="M3 3c0-2 6-2 6 0" fill="none" stroke="#fff" stroke-width="1.2"/></svg>
          <span>555-630-4429</span>
        </li>
      </ul>
    </div>
  </section>

  <section class="card card-back" aria-label="Business card back">
    <div class="frame"></div>
    <div class="motif-row" role="img" aria-label="Row of small green DNA helix ornaments"></div>
    <p class="company-name">CORVALIN</p>
  </section>
</body>
</html>
```